Business Card & Stationary Design Project

We are looking for some creative direction for business cards and our stationary.

We are a global logistics firm that has recently changed its name to Marrick Global Logistics and we have a new website due out tomorrow (www.marrick.com.au).

The colours of the company are rich navy tones, I would like to have business cards that fit together to make one picture on the back (possibly an old map of the world??), and the front to be modern contemporary looking.

But I am open to suggestions, so just incorporate our new logo and get going!
Updates

Hi Everyone,

Thank you for all of your designs so far and the time you have put into it.

I have asked many of you for amendments to see if we can get a final product, so with this in mind I am extending the deadline by a few days.

Good luck and thank you once again.

Please message me direct if you need any clarification.

Kind Regards
Colin

Reason: As outlined the extra 3 days is for amendments and changes to the current submissions. Thanks Colin

Industry/Entity Type

Business

```html
<!DOCTYPE html>
<html lang="en">
<head>
<meta charset="utf-8">
<title>Marrick Global Logistics – Stationery</title>
<link rel="stylesheet" href="https://fonts.googleapis.com/css2?family=Sorts+Mill+Goudy&display=swap">
<style>
  :root {
    --navy-deep: #0c1a4a;
    --navy: #1b3580;
    --navy-bright: #2c4fa8;
    --land: #4a6db0;
    --ink: #000000;
    --paper: #ffffff;
    --canvas: #eef0f2;
    --muted: #b7b7b7;
    --body-ink: #8a8d93;
    --brand-blue: #2a58b8;
    --pale: #e6ecf7;
    --serif: "Sorts Mill Goudy", "Goudy Old Style", Georgia, serif;
  }
  * { box-sizing: border-box; margin: 0; padding: 0; }
  html, body { width: 699px; height: 1200px; overflow: hidden; }
  body {
    background: var(--canvas);
    font-family: var(--serif);
    display: flex;
    flex-direction: column;
    justify-content: space-evenly;
    align-items: center;
  }
  .row { display: flex; gap: 19px; }

  /* company name: one colour, one weight, plain setting */
  .brand { display: flex; align-items: center; gap: 7px; }
  .brand-name {
    font-family: var(--serif);
    font-weight: 400;
    letter-spacing: 0;
    white-space: nowrap;
    line-height: 1;
  }
  .brand-dot { border-radius: 50%; flex: none; }

  /* business card */
  .card { width: 310px; height: 186px; position: relative; overflow: hidden; }
  .card-front { background: var(--ink); color: var(--paper); }
  .card-front .brand { position: absolute; top: 18px; right: 18px; }
  .card-front .brand-name { font-size: 14px; color: var(--paper); }
  .card-front .brand-dot { width: 12px; height: 12px; background: var(--brand-blue); }
  .card-name { position: absolute; top: 68px; left: 10px; font-size: 18px; font-weight: 400; }
  .card-role { position: absolute; top: 92px; left: 10px; font-size: 9px; color: var(--muted); }
  .card-contact {
    position: absolute; top: 128px; left: 10px;
    display: grid; grid-template-columns: 34px auto; row-gap: 5px;
    font-size: 9px;
  }
  .card-contact dt { color: var(--muted); }
  .card-contact dd { font-weight: 700; }
  .card-address {
    position: absolute; top: 136px; right: 14px;
    font-size: 9.5px; font-weight: 700; line-height: 1.35; font-style: normal;
  }
  .map-fill {
    position: absolute; inset: 0;
    background:
      radial-gradient(ellipse at 30% 45%, rgba(74,109,176,0.55), transparent 55%),
      linear-gradient(135deg, var(--navy-bright) 0%, var(--navy) 45%, var(--navy-deep) 100%);
  }
  .card-back .brand, .cover .brand {
    position: absolute; inset: 0; justify-content: center;
  }
  .card-back .brand-name { font-size: 20px; color: var(--pale); }

  /* folder cover & letterhead */
  .sheet { width: 310px; height: 438px; position: relative; overflow: hidden; }
  .cover .brand-name { font-size: 23px; color: var(--pale); }
  .letterhead { background: var(--paper); padding: 22px 26px; box-shadow: 0 1px 3px rgba(0,0,0,0.12); }
  .mini-brand .brand-name { font-size: 8px; color: var(--brand-blue); }
  .mini-brand .brand-dot { width: 8px; height: 8px; background: var(--brand-blue); }
  .letter-date { margin-top: 34px; font-size: 6px; color: var(--body-ink); }
  .letter-salutation { margin-top: 10px; font-size: 8px; color: #333; }
  .letter-body p { margin-top: 9px; font-size: 6.4px; line-height: 1.6; color: var(--body-ink); }
  .letter-footer {
    position: absolute; left: 0; right: 0; bottom: 16px;
    text-align: center; font-size: 6px; font-weight: 700; color: #222; line-height: 1.5;
  }

  /* envelopes */
  .envelope { width: 310px; height: 155px; background: var(--paper); position: relative; box-shadow: 0 1px 3px rgba(0,0,0,0.12); }
  .envelope .mini-brand { position: absolute; }
  .envelope-front .mini-brand { top: 16px; right: 18px; }
  .return-address { position: absolute; top: 16px; left: 16px; font-size: 5px; line-height: 1.6; color: #666; font-style: normal; }
  .envelope-back .flap {
    position: absolute; inset: 0;
    background: linear-gradient(to bottom right, transparent 49.6%, #e3e5e8 50%, transparent 50.4%),
                linear-gradient(to bottom left, transparent 49.6%, #e3e5e8 50%, transparent 50.4%);
    background-size: 50% 60%; background-repeat: no-repeat;
    background-position: left top, right top;
  }
  .envelope-back .mini-brand { bottom: 18px; right: 18px; }
</style>
</head>
<body>

  <section class="row business-cards">
    <article class="card card-front">
      <div class="brand">
        <span class="brand-name">Marrick Global Logistics</span>
        <span class="brand-dot"></span>
      </div>
      <h1 class="card-name">Colin Ashford</h1>
      <p class="card-role">General Manager</p>
      <dl class="card-contact">
        <dt>mail.</dt><dd>colin@marrick.com.au</dd>
        <dt>tel.</dt><dd>+61 2 8000 4127</dd>
        <dt>web.</dt><dd>www.marrick.com.au</dd>
      </dl>
      <address class="card-address">58 Harbour Lane,<br>Pyrmont,<br>NSW, 2009, Australia</address>
    </article>

    <article class="card card-back">
      <div class="map-fill" role="img" aria-label="Navy world map of Asia and Australia with a faint globe grid"></div>
      <div class="brand">
        <span class="brand-name">Marrick Global Logistics</span>
      </div>
    </article>
  </section>

  <section class="row stationery">
    <article class="sheet cover">
      <div class="map-fill" role="img" aria-label="Navy world map of Asia and Australia with a faint globe grid"></div>
      <div class="brand">
        <span class="brand-name">Marrick Global Logistics</span>
      </div>
    </article>

    <article class="sheet letterhead">
      <div class="brand mini-brand">
        <span class="brand-name">Marrick Global Logistics</span>
        <span class="brand-dot"></span>
      </div>
      <p class="letter-date">12 May 2015</p>
      <p class="letter-salutation">Dear Mr. President</p>
      <div class="letter-body">
        <p>Thank you for meeting with our team last week. We are pleased to confirm the freight schedule for your next season of shipments across the Pacific region.</p>
        <p>Our Sydney office will coordinate customs clearance, warehousing and final delivery, and a dedicated account manager will keep you informed at every stage of the journey.</p>
        <p>Please let us know if any details need to change. We look forward to a long partnership.</p>
      </div>
      <footer class="letter-footer">
        www.marrick.com.au<br>
        58 Harbour Lane, Pyrmont, NSW, 2009, Australia
      </footer>
    </article>
  </section>

  <section class="row envelopes">
    <article class="envelope envelope-front">
      <address class="return-address">
        colin@marrick.com.au<br>
        +61 2 8000 4127<br>
        58 Harbour Lane, Pyrmont, NSW, 2009, Australia
      </address>
      <div class="brand mini-brand">
        <span class="brand-name">Marrick Global Logistics</span>
        <span class="brand-dot"></span>
      </div>
    </article>

    <article class="envelope envelope-back">
      <div class="flap"></div>
      <div class="brand mini-brand">
        <span class="brand-name">Marrick Global Logistics</span>
        <span class="brand-dot"></span>
      </div>
    </article>
  </section>

</body>
</html>
```